Logo and Business Card Design

We are macadamia farmers with a network of operations able to deliver macadamia nuts to you!
Be it wholesale or retail supply, our production capacity, network of farms and processing facilities is able to provide reliable and secure supply of macadamia products.
We have a network of owned and contract production macadamia farms located throughout Queensland and New South Wales. Our farms are located in the lush green hinterland area of Northern New south wales and the rich and productive farmlands of the Burnett area of southern Queensland. We pride ourselves on our environmentally sensitive production systems, the ownership and pride in which our network of farmers care for their orchards and the food we produce. Collectively our farms deliver to processing facilities able to provide macadamia nut in shell and kernel in wholesale and retail quantities.
Our point of difference is our integrated supply chain, delivering paddock to plate capacity.
The enterprise is a true network in that we have combined production, processing and marketing expertise into a one stop shop!
Our design should communicate our network capacity, we are a food producer which is respectful of the land and the environment in which we operate.
Our focus is Macadamia nut production, we farm and process Macadamia's where they are a native tree.

The draft design concept we feel is too mechanical and sterile, its time for something fresh and exciting!

Environment

Tellow Grove Pty. Ltd
An Integrated Macadamia production Enterprise.

```html
<!DOCTYPE html>
<html lang="en">
<head>
<meta charset="utf-8">
<title>Tellow Grove – Business Card</title>
<link href="https://fonts.googleapis.com/css2?family=Exo+2:wght@500;700;800&display=swap" rel="stylesheet">
<style>
  :root{
    --bg:#e9e8e5;
    --card-light:#ffffff;
    --card-shade:#dcdcdc;
    --brown:#3e2415;
    --green:#0ea24a;
    --ink:#2a2a2a;
    --white:#ffffff;
  }
  *{margin:0;padding:0;box-sizing:border-box}
  html,body{width:1200px;height:899px;overflow:hidden;background:var(--bg)}
  body{font-family:"Exo 2",sans-serif;position:relative}
  .card{
    position:absolute;left:250px;width:700px;height:400px;overflow:hidden;
    background:radial-gradient(ellipse at 55% 45%,var(--card-light) 30%,var(--card-shade) 100%);
    box-shadow:0 6px 18px rgba(0,0,0,.18);
  }
  .card--back{top:30px}
  .card--front{top:469px}
  .wordmark{
    color:var(--brown);font-weight:800;text-transform:uppercase;
    letter-spacing:1px;line-height:.9;display:flex;align-items:center;gap:12px;
  }
  .wordmark__dot{width:20px;height:20px;border-radius:50%;background:var(--green);flex:none}
  .card--back .wordmark{position:absolute;left:0;right:0;top:160px;justify-content:center;font-size:46px}
  .card__swoosh{position:absolute;inset:0;width:700px;height:400px}
  .card--front .wordmark{position:absolute;left:44px;top:150px;font-size:38px}
  .person{position:absolute;right:36px;top:118px;text-align:right;color:var(--white)}
  .person__name{font-size:25px;font-weight:700;letter-spacing:1.5px;text-transform:uppercase}
  .person__role{font-size:17px;font-weight:500;letter-spacing:1px;margin-top:4px}
  .contacts{position:absolute;left:44px;top:232px;list-style:none;color:var(--ink);font-size:15px;font-weight:500;letter-spacing:.8px}
  .contacts li{display:flex;align-items:center;gap:12px;height:27px}
  .contacts svg{width:16px;height:16px;fill:var(--ink);flex:none}
  .address{position:absolute;right:70px;bottom:26px;text-align:right;color:var(--ink);font-size:18px;font-weight:500;letter-spacing:1px;line-height:1.35}
</style>
</head>
<body>
  <section class="card card--back">
    <div class="wordmark"><span class="wordmark__dot"></span>Tellow Grove</div>
  </section>

  <section class="card card--front">
    <svg class="card__swoosh" viewBox="0 0 700 400" aria-hidden="true">
      <path fill="var(--brown)" d="M0,0 H700 V400 H672 C632,215 420,82 0,90 Z"/>
      <path fill="var(--green)" d="M0,90 C420,82 632,215 672,400 H646 C600,240 420,100 0,98 Z"/>
    </svg>

    <div class="person">
      <div class="person__name">Daniel Hartley</div>
      <div class="person__role">Managing Director</div>
    </div>

    <div class="wordmark"><span class="wordmark__dot"></span>Tellow Grove</div>

    <ul class="contacts">
      <li><svg viewBox="0 0 16 16"><path d="M3 1h3l1 4-2 1c1 2 3 4 5 5l1-2 4 1v3c0 1-1 2-2 2C7 15 1 9 1 3c0-1 1-2 2-2z"/></svg>021 468 3570</li>
      <li><svg viewBox="0 0 16 16"><path d="M4 0h8c1 0 1 1 1 1v14s0 1-1 1H4c-1 0-1-1-1-1V1s0-1 1-1zm1 2v10h6V2zm3 11a1 1 0 100 2 1 1 0 000-2z"/></svg>021 468 3571</li>
      <li><svg viewBox="0 0 16 16"><path d="M2 5h12v9H2zm2-4h8v3H4zm1 6v2h2V7zm4 0v2h2V7zm-4 3v2h2v-2zm4 0v2h2v-2z"/></svg>021 468 3572</li>
      <li><svg viewBox="0 0 16 16"><path d="M1 3h14v10H1zm1 1v1l6 4 6-4V4z"/></svg>hello@tellowgrove.com</li>
      <li><svg viewBox="0 0 16 16"><path d="M8 1a7 7 0 100 14A7 7 0 008 1zm0 1.5c.8 0 1.8 1.9 2 4.5H6c.2-2.6 1.2-4.5 2-4.5zM2.6 7h2.4c.1-1.6.5-3 1-4A5.5 5.5 0 002.6 7zm8.4 0h2.4A5.5 5.5 0 0010 3c.5 1 .9 2.4 1 4zM2.6 9A5.5 5.5 0 006 13c-.5-1-.9-2.4-1-4zm3.4 0c.2 2.6 1.2 4.5 2 4.5s1.8-1.9 2-4.5zm5 0c-.1 1.6-.5 3-1 4a5.5 5.5 0 003.4-4z"/></svg>www.tellowgrove.com</li>
    </ul>

    <div class="address">14 Orchard Lane<br>Gayndah QLD</div>
  </section>
</body>
</html>
```